Steelcrest Process Systems. Needs a Business Card Design

We need a business card design for an engineering company which supplies industrial components (pumps, compressors, mechanical seals) provides repairs and services for above mentioned equipments. We offer a uniqe engineering solutions which help our customers to increase the productivness of their manufacturings, and energy savings.

Target Market(s)

Chemical and energy plants, refineries. Food industry and private consumers in a less.

Industry/Entity Type

Business

Contact Information for Business Card

Stylish and sleek design oriented on industrial area.

Requirements
Should not have
• company name shortening

```html
<!DOCTYPE html>
<html lang="en">
<head>
<meta charset="utf-8">
<title>Steelcrest Process Systems – Business Card</title>
<link rel="stylesheet" href="https://fonts.googleapis.com/css2?family=Open+Sans:wght@400;600;700&display=swap">
<style>
  :root {
    --canvas: #ecebe8;
    --card-light: #ffffff;
    --card-shade: #e4e4e4;
    --ink: #1c1c1c;
    --ink-soft: #333333;
    --brand-blue: #1f3f9a;
    --brand-red: #ef3e36;
    --brand-orange: #f7a823;
    --icon-blue: #3d5ba8;
  }
  * { box-sizing: border-box; margin: 0; padding: 0; }
  html, body { width: 1200px; height: 784px; overflow: hidden; }
  body {
    background: var(--canvas);
    font-family: "Open Sans", Arial, sans-serif;
    color: var(--ink);
    position: relative;
  }
  .card {
    position: absolute;
    width: 540px;
    height: 310px;
    border-radius: 3px;
    overflow: hidden;
    background: radial-gradient(circle at 45% 40%, var(--card-light) 0%, #f6f6f6 45%, var(--card-shade) 100%);
    box-shadow: 0 2px 6px rgba(0,0,0,0.18);
  }
  .card--front { left: 40px; top: 237px; }
  .card--back  { left: 620px; top: 237px; }

  .brand-dot {
    position: absolute;
    border-radius: 50%;
    background: var(--brand-red);
  }
  .brand-name {
    position: absolute;
    font-weight: 700;
    color: var(--ink);
    white-space: nowrap;
    letter-spacing: -0.2px;
  }

  .card--front .brand-dot { width: 54px; height: 54px; left: 243px; top: 70px; }
  .card--front .brand-name { left: 0; width: 100%; text-align: center; top: 138px; font-size: 27px; }

  .card--back .brand-dot { width: 42px; height: 42px; left: 130px; top: 58px; }
  .card--back .brand-name { left: 40px; top: 110px; font-size: 21px; }

  .holder {
    position: absolute;
    right: 24px;
    top: 20px;
    text-align: right;
  }
  .holder__name { font-weight: 700; font-size: 14px; color: var(--brand-blue); letter-spacing: 0.3px; }
  .holder__role { font-size: 9px; color: var(--ink-soft); margin-top: -1px; }

  .contact-list {
    position: absolute;
    left: 40px;
    top: 152px;
    list-style: none;
    font-size: 12px;
    line-height: 16px;
    color: var(--ink-soft);
    z-index: 1;
  }
  .contact-list li { display: flex; align-items: center; gap: 7px; height: 16px; }
  .contact-list svg { width: 11px; height: 11px; flex: none; }
  .contact-list .no-icon { padding-left: 18px; }

  .accent-area {
    position: absolute;
    left: 0;
    right: 0;
    bottom: 0;
    height: 60px;
    background: linear-gradient(90deg,
      rgba(239,62,54,0.22) 0%,
      rgba(247,168,35,0.22) 55%,
      rgba(31,63,154,0.28) 100%);
  }
</style>
</head>
<body>

<section class="card card--front" aria-label="Card front">
  <span class="brand-dot"></span>
  <p class="brand-name">Steelcrest Process Systems</p>
</section>

<section class="card card--back" aria-label="Card back">
  <div class="accent-area" role="img" aria-label="Decorative flowing ribbons in red, orange and blue"></div>

  <div class="holder">
    <p class="holder__name">MARCUS HALE</p>
    <p class="holder__role">Manager</p>
  </div>

  <span class="brand-dot"></span>
  <p class="brand-name">Steelcrest Process Systems</p>

  <ul class="contact-list">
    <li>
      <svg viewBox="0 0 12 12" aria-hidden="true"><rect x="3" y="0.5" width="6" height="11" rx="1.2" fill="var(--icon-blue)"/><rect x="4" y="2" width="4" height="6" fill="#fff"/></svg>
      0412 555 019
    </li>
    <li>
      <svg viewBox="0 0 12 12" aria-hidden="true"><path d="M1 4 C1 2 3 1.5 6 1.5 C9 1.5 11 2 11 4 L9 5 L8 3.5 L4 3.5 L3 5 Z" fill="var(--icon-blue)"/><rect x="2" y="6" width="8" height="5" rx="1" fill="var(--icon-blue)"/></svg>
      +61 7 3555 0148
    </li>
    <li>
      <svg viewBox="0 0 12 12" aria-hidden="true"><rect x="0.5" y="2.5" width="11" height="7.5" rx="1" fill="var(--icon-blue)"/><path d="M1 3 L6 7 L11 3" stroke="#fff" stroke-width="1" fill="none"/></svg>
      marcus@steelcrestprocess.com
    </li>
    <li>
      <svg viewBox="0 0 12 12" aria-hidden="true"><circle cx="6" cy="6" r="5.2" fill="var(--icon-blue)"/><path d="M1 6 H11 M6 1 C3.5 3.5 3.5 8.5 6 11 M6 1 C8.5 3.5 8.5 8.5 6 11" stroke="#fff" stroke-width="0.7" fill="none"/></svg>
      www.steelcrestprocess.com
    </li>
    <li>
      <svg viewBox="0 0 12 12" aria-hidden="true"><path d="M6 1 L11.5 6 L10 6 L10 11 L7.3 11 L7.3 8 L4.7 8 L4.7 11 L2 11 L2 6 L0.5 6 Z" fill="var(--icon-blue)"/></svg>
      14 Foundry Rd Coopers Plains
    </li>
    <li class="no-icon">ABN 41 062 318 907</li>
  </ul>
</section>

</body>
</html>
```